New Web 2.0 responsive website for popup advertisement network

We need a responsive web design for a new popup advertisement network company Clikvantra.com based in Newport Beach, California.

We need the design for the main site as well as the interface design for the member portal login area.

Below is the requirement and concept for the website / portal. 

1. With reference to http://tabrivex.com/  (Overall  home layout design and menu bar can follow this website (except the homepage banner section) ,color theme change to #81D8D0)

2. Integrate 3 step process in the homepage for easy reference. Follow the concept in the website below but use better graphic and images to present. Can integrate this in homepage banner section.
   reference:  http://quorlent.net/, http://zandimex.com/ 

3.  Use the nice look ad tag line in the homepage banner section as well. Can refer to the site below.
     http://www.yieldbarrow.com/#publishers
 
4. Sign up button must be clear and obvious in the homepage.

We required the design for the pages below.
1. Homepage
2. Dashboard
3. Add Website
3. Code Generator
4. Website
5. Report

(Please refer to the attached image for the concept and field required in the page)

Target Market(s)

US, web owner such as blogger or content sites

Industry/Entity Type

Advertising

Logo Text

Scientific and Fun

Coding

Coded - Design and coding required

Number of Pages Required

5+ page

Font styles to use
Sans Serif

Colors
0692cd

```html
<!DOCTYPE html>
<html lang="en">
<head>
<meta charset="utf-8">
<title>Clikvantra – Popup Advertisement Network</title>
<link href="https://fonts.googleapis.com/css2?family=Hind:wght@300;400;500;600;700&display=swap" rel="stylesheet">
<style>
:root{
  --blue:#0692cd;
  --teal:#81d8d0;
  --ink:#3a3a3a;
  --muted:#8d8d8d;
  --line:#e4e4e4;
  --white:#ffffff;
  --footer:#0a8fce;
  --band:#1a1e28;
  --btn-dark:#2f3338;
}
*{margin:0;padding:0;box-sizing:border-box}
html,body{width:1200px;height:2326px;overflow:hidden}
body{font-family:"Hind",Arial,sans-serif;color:var(--ink);background:var(--white);position:relative}
.abs{position:absolute}
.center{text-align:center}

/* header */
.site-header{position:absolute;left:0;top:0;width:1200px;height:82px;background:var(--white)}
.brand{position:absolute;left:99px;top:27px;font-size:27px;font-weight:600;color:var(--blue);letter-spacing:.2px}
.main-nav a{position:absolute;top:32px;font-size:13px;color:#8a8a8a;text-decoration:none;letter-spacing:.6px}
.main-nav a.active{color:#222;font-weight:500}
.signup{position:absolute;left:1020px;top:25px;width:81px;height:32px;border-radius:16px;background:var(--blue);color:var(--white);font-size:13px;font-weight:600;line-height:34px;text-align:center;letter-spacing:.5px}

/* hero */
.hero{position:absolute;left:0;top:82px;width:1200px;height:569px;overflow:hidden}
.hero-photo{position:absolute;inset:0;background:radial-gradient(ellipse at 60% 45%,#8a5a44 0%,#5b3a2c 45%,#2e211c 100%)}
.hero-shade{position:absolute;inset:0;background:rgba(25,15,10,.35)}
.hero-title{position:absolute;left:0;top:112px;width:1200px;text-align:center;color:var(--white);font-size:45px;font-weight:700;line-height:54px;letter-spacing:.5px}
.slide-arrow{position:absolute;top:253px;width:62px;height:62px;border-radius:50%;border:2px solid rgba(255,255,255,.55)}
.step{position:absolute;top:287px;width:134px;height:134px;border-radius:50%;background:var(--teal);border:5px solid var(--white)}
.step svg{position:absolute;left:42px;top:42px}
.step-label{position:absolute;top:436px;width:300px;text-align:center;color:var(--white);font-size:20px;font-weight:500;letter-spacing:.4px}

/* audience */
.aud-icon{position:absolute;top:680px;width:146px;height:146px;border-radius:50%}
.aud-title{position:absolute;top:848px;width:500px;text-align:center;font-size:26px;font-weight:500;letter-spacing:.6px;color:#333}
.aud-text{position:absolute;top:903px;width:420px;text-align:center;font-size:12.5px;line-height:21.5px;color:var(--muted)}
.read-more{position:absolute;top:1014px;width:112px;height:34px;border-radius:17px;color:var(--white);font-size:13px;font-weight:600;line-height:36px;text-align:center;letter-spacing:.3px}
.divider{position:absolute;left:99px;top:1099px;width:1002px;height:1px;background:var(--line)}

/* features */
.section-title{position:absolute;left:0;width:1200px;text-align:center;font-size:25px;font-weight:500;color:#333;letter-spacing:.4px}
.feature{position:absolute;width:300px}
.feature svg{position:absolute;left:0;top:0}
.feature h3{position:absolute;left:48px;top:4px;font-size:18px;font-weight:400;color:#333;white-space:nowrap}
.feature p{position:absolute;left:0;top:46px;width:300px;font-size:12.5px;line-height:21px;color:var(--muted)}

/* cta band */
.cta{position:absolute;left:0;top:1530px;width:1200px;height:295px;overflow:hidden}
.cta-photo{position:absolute;inset:0;background:linear-gradient(180deg,#2a3140 0%,#151a24 100%)}
.cta-text{position:absolute;left:0;top:70px;width:1200px;text-align:center;color:var(--white);font-size:24px;font-weight:500;line-height:36px;letter-spacing:.5px}
.cta-btn{position:absolute;left:432px;top:166px;width:335px;height:51px;border:2px solid var(--white);border-radius:26px;color:var(--white);text-align:center;font-size:16px;font-weight:600;line-height:51px;letter-spacing:.5px}

/* insights */
.stat{position:absolute;top:1940px;width:180px;text-align:center}
.stat svg{display:block;margin:0 auto}
.stat .num{font-size:36px;font-weight:300;color:#444;margin-top:14px;line-height:40px}
.stat .label{font-size:12px;color:var(--muted);margin-top:8px}

/* footer */
.site-footer{position:absolute;left:0;top:2108px;width:1200px;height:218px;background:var(--footer);color:var(--white)}
.site-footer h4{position:absolute;top:35px;font-size:14px;font-weight:600;letter-spacing:.5px}
.vline{position:absolute;top:40px;width:1px;height:150px;background:rgba(255,255,255,.25)}
.social{position:absolute;top:77px;width:32px;height:32px;border-radius:50%;border:2px solid var(--white)}
.foot-small{position:absolute;font-size:11.5px;line-height:20px}
.foot-links{position:absolute;left:742px;top:72px;list-style:none;font-size:10.5px;line-height:21px;letter-spacing:.3px}
.news-input{position:absolute;left:907px;top:69px;width:194px;height:31px;background:var(--white);color:#777;font-size:11px;line-height:32px;padding-left:10px}
.submit{position:absolute;left:997px;top:112px;width:104px;height:34px;border-radius:17px;background:var(--btn-dark);color:var(--white);font-size:12px;font-weight:600;line-height:36px;text-align:center;letter-spacing:.5px}
</style>
</head>
<body>

<header class="site-header">
  <div class="brand">Clikvantra</div>
  <nav class="main-nav">
    <a class="active" style="left:499px">HOME</a>
    <a style="left:581px">PUBLISHERS</a>
    <a style="left:701px">ADVERTISERS</a>
    <a style="left:829px">REGULATION</a>
    <a style="left:953px">BLOG</a>
  </nav>
  <div class="signup">SIGN UP</div>
</header>

<section class="hero">
  <div class="hero-photo" role="img" aria-label="Blurred photo of hands holding a smartphone next to a laptop"></div>
  <div class="hero-shade"></div>
  <h1 class="hero-title">AT VERO EOS ET ACCUSAMUS ET<br>IUSTO ODIO DIGNISSIMOS</h1>

  <div class="slide-arrow" style="left:36px">
    <svg width="58" height="58" viewBox="0 0 58 58"><path d="M32 20 L23 29 L32 38" fill="none" stroke="#fff" stroke-width="2"/></svg>
  </div>
  <div class="slide-arrow" style="left:1105px">
    <svg width="58" height="58" viewBox="0 0 58 58"><path d="M26 20 L35 29 L26 38" fill="none" stroke="#fff" stroke-width="2"/></svg>
  </div>

  <svg class="abs" style="left:0;top:0" width="1200" height="569" viewBox="0 0 1200 569">
    <path d="M414 382 C440 410 470 380 510 366" fill="none" stroke="#fff" stroke-width="3"/>
    <path d="M498 358 L512 365 L500 376" fill="none" stroke="#fff" stroke-width="3"/>
    <path d="M660 320 C700 290 740 300 782 336" fill="none" stroke="#fff" stroke-width="3"/>
    <path d="M766 332 L783 338 L776 322" fill="none" stroke="#fff" stroke-width="3"/>
  </svg>

  <div class="step" style="left:282px">
    <svg width="40" height="40" viewBox="0 0 40 40"><path d="M8 32 L10 24 L26 8 L32 14 L16 30 Z" fill="#fff"/></svg>
  </div>
  <div class="step" style="left:528px">
    <svg width="40" height="40" viewBox="0 0 40 40"><circle cx="20" cy="16" r="9" fill="none" stroke="#fff" stroke-width="3"/><rect x="16" y="26" width="8" height="7" fill="#fff"/></svg>
  </div>
  <div class="step" style="left:783px">
    <svg width="40" height="40" viewBox="0 0 40 40"><rect x="4" y="10" width="32" height="20" fill="#fff"/><circle cx="20" cy="20" r="5" fill="#81d8d0"/></svg>
  </div>

  <div class="step-label" style="left:199px">REGISTER</div>
  <div class="step-label" style="left:445px">SHOW RELEVANT ADS</div>
  <div class="step-label" style="left:700px">EARN MONEY</div>
</section>

<section class="audience">
  <div class="aud-icon" style="left:249px;background:var(--blue)">
    <svg class="abs" style="left:45px;top:48px" width="56" height="50" viewBox="0 0 56 50"><path d="M6 18 H16 L40 6 V44 L16 32 H6 Z" fill="#fff"/><path d="M14 32 L20 46 H26 L22 32 Z" fill="#fff"/><rect x="44" y="20" width="6" height="10" fill="#fff"/></svg>
  </div>
  <div class="aud-icon" style="left:777px;background:var(--teal)">
    <svg class="abs" style="left:53px;top:44px" width="40" height="56" viewBox="0 0 40 56"><path d="M2 2 H26 L38 14 V54 H2 Z" fill="#fff"/><rect x="9" y="24" width="22" height="3" fill="#81d8d0"/><rect x="9" y="32" width="22" height="3" fill="#81d8d0"/><rect x="9" y="40" width="22" height="3" fill="#81d8d0"/></svg>
  </div>

  <h2 class="aud-title" style="left:73px">ADVERTISERS</h2>
  <h2 class="aud-title" style="left:600px">PUBLISHERS</h2>

  <p class="aud-text" style="left:113px">At vero eos et accusamus et iusto odio dignissimos ducimus qui blanditiis praesentium voluptatum deleniti atque corrupti quos dolores et quas molestias excepturi sint occaecati cupiditate non provident, similique sunt in culpa qui officia deserunt mollitia</p>
  <p class="aud-text" style="left:640px">At vero eos et accusamus et iusto odio dignissimos ducimus qui blanditiis praesentium voluptatum deleniti atque corrupti quos dolores et quas molestias excepturi sint occaecati cupiditate non provident, similique sunt in culpa qui officia deserunt mollitia</p>

  <div class="read-more" style="left:267px;background:var(--blue)">READ MORE</div>
  <div class="read-more" style="left:794px;background:var(--teal)">READ MORE</div>
  <div class="divider"></div>
</section>

<section class="features">
  <h2 class="section-title" style="top:1165px">CLIKVANTRA FEATURES</h2>

  <div class="feature" style="left:99px;top:1250px">
    <svg width="34" height="34" viewBox="0 0 34 34"><circle cx="17" cy="17" r="14" fill="none" stroke="#0692cd" stroke-width="3.5"/><path d="M17 9 V17 H23" fill="none" stroke="#0692cd" stroke-width="3"/></svg>
    <h3>Realtime bidding system</h3>
    <p>Sed ut perspiciatis unde omnis iste natus error sit voluptatem accusantium doloremque lauda.</p>
  </div>
  <div class="feature" style="left:450px;top:1250px">
    <svg width="36" height="34" viewBox="0 0 36 34"><path d="M4 20 L20 4 L32 16 L16 32 Z" fill="#0692cd"/><path d="M12 20 L20 12" stroke="#fff" stroke-width="2"/></svg>
    <h3>Dedicated account manager</h3>
    <p>Sed ut perspiciatis unde omnis iste natus error sit voluptatem accusantium doloremque lauda.</p>
  </div>
  <div class="feature" style="left:811px;top:1250px">
    <svg width="34" height="34" viewBox="0 0 34 34"><circle cx="17" cy="17" r="12" fill="none" stroke="#0692cd" stroke-width="7"/><path d="M9 9 L13 13 M25 9 L21 13 M9 25 L13 21 M25 25 L21 21" stroke="#fff" stroke-width="3"/></svg>
    <h3>24/7 support</h3>
    <p>Sed ut perspiciatis unde omnis iste natus error sit voluptatem accusantium doloremque lauda.</p>
  </div>
  <div class="feature" style="left:99px;top:1371px">
    <svg width="38" height="34" viewBox="0 0 38 34"><path d="M3 3 V31 H36" fill="none" stroke="#0692cd" stroke-width="2.5"/><rect x="8" y="16" width="4" height="13" fill="#0692cd"/><rect x="15" y="10" width="4" height="19" fill="#0692cd"/><rect x="22" y="14" width="4" height="15" fill="#0692cd"/><rect x="29" y="7" width="4" height="22" fill="#0692cd"/></svg>
    <h3>Realtime reports</h3>
    <p>Sed ut perspiciatis unde omnis iste natus error sit voluptatem accusantium doloremque lauda.</p>
  </div>
  <div class="feature" style="left:450px;top:1371px">
    <svg width="36" height="34" viewBox="0 0 36 34"><rect x="2" y="5" width="32" height="24" rx="3" fill="none" stroke="#0692cd" stroke-width="3"/><rect x="2" y="11" width="32" height="4" fill="#0692cd"/><rect x="7" y="21" width="8" height="3" fill="#0692cd"/></svg>
    <h3>Instant deposits / withdraws</h3>
    <p>Sed ut perspiciatis unde omnis iste natus error sit voluptatem accusantium doloremque lauda.</p>
  </div>
  <div class="feature" style="left:811px;top:1371px">
    <svg width="34" height="34" viewBox="0 0 34 34"><g fill="#0692cd"><circle cx="17" cy="17" r="11"/><rect x="14" y="1" width="6" height="32"/><rect x="1" y="14" width="32" height="6"/><rect x="14" y="1" width="6" height="32" transform="rotate(45 17 17)"/><rect x="14" y="1" width="6" height="32" transform="rotate(-45 17 17)"/></g><circle cx="17" cy="17" r="5" fill="#fff"/></svg>
    <h3>Full control</h3>
    <p>Sed ut perspiciatis unde omnis iste natus error sit voluptatem accusantium doloremque lauda.</p>
  </div>
</section>

<section class="cta">
  <div class="cta-photo" role="img" aria-label="Blurred dark photo of a laptop on a desk"></div>
  <p class="cta-text">AT VERO EOS ET ACCUSAMUS ET IUSTO ODIO DIGNISSIMOS DUCIMUS QUI<br>EXCEPTURI SINT OCCA NEW POPUP ADVERTISEMENT NETWORK.</p>
  <div class="cta-btn">GO TO POPUP ADVERTISEMENT</div>
</section>

<section class="insights">
  <h2 class="section-title" style="top:1872px">NETWORK INSIGHTS</h2>
  <div class="stat" style="left:135px">
    <svg width="28" height="28" viewBox="0 0 28 28"><circle cx="14" cy="14" r="13" fill="#0692cd"/><path d="M8 7 C12 9 10 13 14 14 C16 16 12 20 15 25 M18 4 C17 8 22 9 24 12" fill="none" stroke="#fff" stroke-width="2"/></svg>
    <div class="num">214</div><div class="label">WEBSITES</div>
  </div>
  <div class="stat" style="left:322px">
    <svg width="30" height="28" viewBox="0 0 30 28"><rect x="1" y="7" width="28" height="20" rx="3" fill="#0692cd"/><rect x="10" y="2" width="10" height="7" fill="none" stroke="#0692cd" stroke-width="2.5"/></svg>
    <div class="num">22086</div><div class="label">WEBSITES</div>
  </div>
  <div class="stat" style="left:510px">
    <svg width="28" height="28" viewBox="0 0 28 28"><circle cx="14" cy="14" r="13" fill="#0692cd"/><path d="M8 7 C12 9 10 13 14 14 C16 16 12 20 15 25 M18 4 C17 8 22 9 24 12" fill="none" stroke="#fff" stroke-width="2"/></svg>
    <div class="num">342</div><div class="label">WEBSITES</div>
  </div>
  <div class="stat" style="left:699px">
    <svg width="24" height="30" viewBox="0 0 24 30"><circle cx="12" cy="11" r="9" fill="none" stroke="#0692cd" stroke-width="2.5"/><rect x="8" y="21" width="8" height="7" fill="#0692cd"/></svg>
    <div class="num">17520</div><div class="label">Clients</div>
  </div>
  <div class="stat" style="left:891px">
    <svg width="26" height="28" viewBox="0 0 26 28"><circle cx="13" cy="8" r="7" fill="#0692cd"/><path d="M1 28 C1 18 25 18 25 28 Z" fill="#0692cd"/></svg>
    <div class="num">1478</div><div class="label">Clients</div>
  </div>
</section>

<footer class="site-footer">
  <h4 style="left:99px">FOLLOW US</h4>
  <div class="social" style="left:97px"></div>
  <div class="social" style="left:136px"></div>
  <div class="social" style="left:175px"></div>
  <div class="social" style="left:214px"></div>
  <div class="social" style="left:253px"></div>
  <p class="foot-small" style="left:99px;top:138px">Copyright © 2015 Clikvantra<br>All copyrights are Reserved.</p>

  <div class="vline" style="left:349px"></div>
  <h4 style="left:389px;font-weight:500">GET IN TOUCH</h4>
  <p class="foot-small" style="left:389px;top:68px">48 Harbor Lane, Newport Beach - 92660.<br>&nbsp;Phone : 949-555-0142, 555,0143<br>Fax : 949-555-0199<br>Email : hello@clikvantra.com</p>

  <div class="vline" style="left:667px"></div>
  <h4 style="left:740px">LINKS</h4>
  <ul class="foot-links">
    <li>HOME</li><li>ABOUT US</li><li>SERVICES</li><li>NEWS</li><li>CONTACT US</li>
  </ul>

  <div class="vline" style="left:856px"></div>
  <h4 style="left:907px">NEWSLETTER</h4>
  <div class="news-input">Email</div>
  <div class="submit">SUBMIT</div>
</footer>

</body>
</html>
```